Book jacket for Drumlore

We need a book jacket design (hard cover front, back, spine, flaps; soft cover and eBook). for a social psychology book with the general cluelessness (being "out of it") of how people function both in their personal and social lives. This is the third book written by the author, a practicing psychiatrist, and the content centers on a single subject, people's lack of genuine emotional contact, their cluelessness with themselves and with current national and world events.

Target Market(s)

People who want to better understand the state the nation and world is in now, and what they can do about it.

Font styles to use
Serif
Sans Serif

Requirements
Must have
• Bold, eye-catching cover
Nice to have
• Like the idea of separating the title word (drum lore) to better emphasize the concept of lack of contact

```html
<!DOCTYPE html>
<html lang="en">
<head>
<meta charset="utf-8">
<title>Drumlore — Book Cover</title>
<link rel="stylesheet" href="https://fonts.googleapis.com/css2?family=Bebas+Neue&family=Montserrat:wght@400&family=Poppins:ital,wght@1,300&display=swap">
<style>
  :root {
    --paper: #f6f6f5;
    --slate: #4c4d45;
    --slate-deep: #393a31;
    --signal-red: #e8363f;
    --quote-ink: #ecece8;
  }
  * { margin: 0; padding: 0; box-sizing: border-box; }
  html, body {
    width: 1000px;
    height: 1200px;
    overflow: hidden;
    background: var(--paper);
  }
  .cover {
    position: relative;
    width: 1000px;
    height: 1200px;
    background: var(--paper);
  }
  .cover-blocks {
    position: absolute;
    inset: 0;
  }
  .block-upper { fill: var(--slate); }
  .block-lower { fill: var(--slate-deep); }
  .title-word {
    font-family: "Bebas Neue", "Oswald", sans-serif;
    font-size: 520px;
  }
  .title-first { fill: var(--slate-deep); }
  .title-second { fill: var(--signal-red); }
  .pull-quote {
    position: absolute;
    left: 590px;
    top: 100px;
    width: 370px;
    font-family: "Poppins", sans-serif;
    font-style: italic;
    font-weight: 300;
    font-size: 25px;
    line-height: 1.3;
    color: var(--quote-ink);
  }
  .pull-quote-mark {
    position: absolute;
    left: -42px;
    top: -34px;
    font-family: "Bebas Neue", sans-serif;
    font-style: normal;
    font-size: 140px;
    line-height: 1;
    color: var(--signal-red);
  }
  .author-name {
    position: absolute;
    left: 70px;
    top: 1090px;
    font-family: "Montserrat", sans-serif;
    font-weight: 400;
    font-size: 30px;
    letter-spacing: 0.14em;
    color: var(--signal-red);
    text-transform: uppercase;
  }
</style>
</head>
<body>
  <main class="cover">
    <svg class="cover-blocks" width="1000" height="1200" viewBox="0 0 1000 1200" aria-labelledby="cover-title">
      <title id="cover-title">Drum lore</title>
      <polygon class="block-upper" points="520,0 1000,0 1000,660 710,660 710,540 520,540"/>
      <polygon class="block-lower" points="0,640 310,640 310,790 520,790 520,1200 0,1200"/>
      <text class="title-word title-first" x="148" y="632" textLength="368" lengthAdjust="spacingAndGlyphs">DRUM</text>
      <text class="title-word title-second" x="526" y="866" textLength="354" lengthAdjust="spacingAndGlyphs">LORE</text>
    </svg>

    <blockquote class="pull-quote">
      <span class="pull-quote-mark" aria-hidden="true">&ldquo;</span>
      Lorem ipsum dolor sit amet, consectetur adipiscing elit, sed do eiusmod tempor incididunt ut labore et dolore magna
    </blockquote>

    <p class="author-name">Martin Elward M.D.</p>
  </main>
</body>
</html>
```